Redesign of pixelmentors.net including blog.

We now have a design in layered PSD files. The design is almost there but needs some tweaking and some great coding to get it in place!

We no longer need SEO help, just brilliant coding and some design tweaks.

Please feel free to ask me any questions.

Please note:
1. This is my first time using artflockly, and as such, am not yet ready to make this a guaranteed project. I'm sure I'll be able to do that on subsequent projects when I gain more trust in the process.
2. My clients are always looking for good designers. Always. What I'm doing here is testing the process for myself. If I'm happy with your design and your work ethic, be sure that I'll be sending more work your way.

Thanks for your interest in the project.
Updates

Hello Designers! The project is now GUARANTEED!

Industry/Entity Type

Seo

Requirements
Must have
• * Same idea of having image sliders on the homepage
* Must be smartphone compatible
* High resolution images and icons supporting retina display

```html
<!DOCTYPE html>
<html lang="en">
<head>
<meta charset="utf-8">
<title>PixelMentors</title>
<link href="https://fonts.googleapis.com/css2?family=Ubuntu:wght@300;400;500&family=PT+Sans:wght@400;700&display=swap" rel="stylesheet">
<style>
:root{
  --navy:#3d5270;
  --navy-dark:#34475f;
  --text:#3c5475;
  --body:#4c6280;
  --hero-top:#e3e7ee;
  --hero-bottom:#d4dae4;
  --section:#eef0f4;
  --footer:#2b2b2b;
  --footer-text:#e6e6e6;
  --brand:#555b66;
  --white:#ffffff;
}
*{box-sizing:border-box;margin:0;padding:0}
html,body{width:977px;height:1200px;overflow:hidden;background:var(--white)}
body{position:relative;font-family:"PT Sans",sans-serif;color:var(--body)}
.abs{position:absolute}

.site-header{position:absolute;left:0;top:0;width:977px;height:109px;border-top:3px solid var(--navy-dark);background:var(--white)}
.brand{position:absolute;left:106px;top:78px;font-family:"PT Sans",sans-serif;font-size:11px;color:var(--brand)}
.utility-links{position:absolute;right:100px;top:11px;font-size:9.5px;color:var(--text)}
.utility-links span{margin:0 5px;color:#8a96a8}
.search{position:absolute;left:689px;top:66px;width:196px;height:24px;border:1px solid #d3d7de;font-size:9.5px;color:#7d8796;padding:5px 10px;box-shadow:0 6px 6px -6px rgba(0,0,0,.15)}
.search svg{position:absolute;right:8px;top:5px}

.main-nav{position:absolute;left:0;top:109px;width:977px;height:46px;background:linear-gradient(#eef0f4,#e4e8ee);border-bottom:1px solid #d8dde5}
.main-nav ul{list-style:none;display:flex;align-items:center;position:absolute;left:91px;top:9px;height:25px;font-family:"Ubuntu",sans-serif;font-size:11px;color:var(--navy-dark)}
.main-nav li{padding:0 17px;border-left:1px solid #9aa6b8;line-height:15px;white-space:nowrap}
.main-nav li.home{border:0;background:var(--navy);color:var(--white);border-radius:13px;padding:5px 19px;margin-right:2px}
.main-nav li.after-home{border-left:0}

.hero{position:absolute;left:0;top:155px;width:977px;height:316px;background:linear-gradient(var(--hero-top),var(--hero-bottom));overflow:hidden}
.cloud{position:absolute;border-radius:50%;background:rgba(255,255,255,.55)}
.hero-copy{position:absolute;left:136px;top:66px;font-family:"Ubuntu",sans-serif;font-weight:300;font-size:21px;line-height:32px;color:var(--text)}
.hero-cta{position:absolute;left:134px;top:179px;width:105px;height:42px;background:var(--navy);color:var(--white);font-family:"Ubuntu",sans-serif;font-weight:300;font-size:24px;line-height:42px;padding-left:20px;box-shadow:0 6px 8px -4px rgba(0,0,0,.25)}
.hero-art{position:absolute;left:556px;top:16px;width:264px;height:281px;border-radius:20px;background:radial-gradient(circle at 50% 40%,#f1d0b0 0,#d8dee8 55%,transparent 75%)}
.slider-dots{position:absolute;left:438px;top:296px}

.projects{position:absolute;left:0;top:471px;width:977px;height:223px;background:var(--section);border-top:1px solid #cfd5de}
.project{position:absolute;top:20px}
.project-thumb{border:3px solid var(--white);height:113px}
.project-title{font-family:"Ubuntu",sans-serif;font-weight:400;font-size:13.5px;color:var(--text);margin:10px 0 5px 2px}
.project-text{font-size:9.4px;line-height:15px;margin-left:2px}

.welcome{position:absolute;left:85px;top:722px;width:528px}
.section-title{font-family:"Ubuntu",sans-serif;font-weight:300;font-size:18px;color:var(--text);margin-bottom:12px}
.welcome p{font-size:9.4px;line-height:15px;margin-left:3px;margin-bottom:15px}
.read-more{font-family:"Ubuntu",sans-serif;font-weight:300;font-size:13px;color:var(--text);margin-left:5px}

.sidebar-divider{position:absolute;left:629px;top:694px;width:1px;height:383px;background:linear-gradient(#fff,#dfe3e9 30%,#dfe3e9 80%,#fff)}
.blog-feed{position:absolute;left:649px;top:722px;width:236px}
.blog-feed .section-title{display:flex;align-items:center;gap:10px;margin-bottom:14px}
.feed-dot{width:28px;height:17px;border-radius:50%;background:#111}
.post{margin-bottom:17px}
.post h3{font-family:"Ubuntu",sans-serif;font-weight:300;font-size:12px;color:var(--text);margin-bottom:5px}
.post p{font-size:9.4px;line-height:15px;margin-bottom:8px}
.post-meta{font-size:9px;font-weight:700;color:var(--navy-dark);margin-left:-1px}
.post-meta span{margin:0 8px;font-weight:400}

.site-footer{position:absolute;left:0;top:1077px;width:977px;height:123px;background:var(--footer);color:var(--footer-text)}
.footer-links{position:absolute;left:85px;top:22px;font-size:10.5px}
.footer-links span{margin:0 6px;color:#aaa}
.copyright{position:absolute;left:85px;top:50px;font-size:9.5px}
.social{position:absolute;left:779px;top:20px;display:flex;gap:4px}
.social span{width:26px;height:26px;border-radius:50%;background:#e9e9e9}
</style>
</head>
<body>

<header class="site-header">
  <div class="brand">pixelmentors</div>
  <div class="utility-links">Contact<span>|</span>Blog<span>|</span>Sitemap</div>
  <div class="search">Enter keyword
    <svg width="16" height="14" viewBox="0 0 16 14"><circle cx="6" cy="6" r="4.5" fill="none" stroke="#b9c0ca" stroke-width="1.5"/><line x1="9.5" y1="9" x2="14" y2="13" stroke="#b9c0ca" stroke-width="2"/></svg>
  </div>
</header>

<nav class="main-nav">
  <ul>
    <li class="home">HOME</li>
    <li class="after-home">WEB DEVELOPMENT</li>
    <li>SOCIAL MEDIA</li>
    <li>SERVER MANAGEMENT</li>
    <li>CLOUDS DEPLOYMENT</li>
    <li>CODE REVIEW</li>
  </ul>
</nav>

<section class="hero">
  <div class="cloud" style="left:-40px;top:200px;width:200px;height:160px"></div>
  <div class="cloud" style="left:120px;top:250px;width:260px;height:160px"></div>
  <div class="cloud" style="left:330px;top:200px;width:180px;height:180px"></div>
  <div class="cloud" style="left:560px;top:240px;width:260px;height:140px"></div>
  <div class="cloud" style="left:820px;top:190px;width:220px;height:200px"></div>
  <svg class="abs" style="left:75px;top:92px" width="26" height="84" viewBox="0 0 26 84"><polyline points="25,1 1,42 25,83" fill="none" stroke="#5b6f8c" stroke-width="1"/></svg>
  <svg class="abs" style="left:868px;top:92px" width="26" height="84" viewBox="0 0 26 84"><polyline points="1,1 25,42 1,83" fill="none" stroke="#5b6f8c" stroke-width="1"/></svg>
  <div class="hero-copy">Is Your Code Secure?<br>Do You Know what a SQL injection is?<br>If you don't Know, that's fine.</div>
  <div class="hero-cta">We do</div>
  <div class="hero-art" role="img" aria-label="Cartoon developer holding a laptop and a pencil"></div>
  <svg class="slider-dots" width="100" height="20" viewBox="0 0 100 20">
    <path d="M0,20 C20,20 20,2 40,2 L60,2 C80,2 80,20 100,20 Z" fill="#3d5270"/>
    <circle cx="35" cy="11" r="3" fill="#fff"/><circle cx="45" cy="11" r="3" fill="#fff"/><circle cx="55" cy="11" r="3" fill="#fff"/><circle cx="65" cy="11" r="3" fill="#fff"/>
  </svg>
</section>

<section class="projects">
  <article class="project" style="left:92px;width:334px">
    <div class="project-thumb" role="img" aria-label="Website shown on several screens and devices" style="background:linear-gradient(#e8f1f1,#d1dcdc)"></div>
    <h3 class="project-title">Project tittle</h3>
    <p class="project-text">PixelMentors is elastic and extensible, providing our customers with all the necessary resources to complete their requirements on budget and on time.</p>
  </article>
  <article class="project" style="left:445px;width:183px">
    <div class="project-thumb" role="img" aria-label="Open box with a globe and web platform symbols" style="background:linear-gradient(135deg,#2b8fd8,#6cc3f0)"></div>
    <h3 class="project-title">Project tittle</h3>
    <p class="project-text">PixelMentors is elastic and extensible, providing our customers</p>
  </article>
  <article class="project" style="left:647px;width:233px">
    <div class="project-thumb" role="img" aria-label="Two hands joining blue puzzle pieces" style="background:linear-gradient(135deg,#dfe4ef,#2c4a8c 60%,#cfd6e2)"></div>
    <h3 class="project-title">Project tittle</h3>
    <p class="project-text">PixelMentors is elastic and extensible, providing our customers</p>
  </article>
</section>

<main class="welcome">
  <h2 class="section-title">Welcome to Pixelmentors Website Mainpage</h2>
  <p>PixelMentors, a team of 1 that can expand to 100 people in 5 seconds flat.<br>PixelMentors is elastic and extensible, providing our customers with all the necessary resources to complete their require-ments on budget and on time.<br>Brightlane Studio is a professional website design company dedicated to provide excellent services. We at Brightlane Studio think graphic design as a combination and collaboration of ideas and technology. Our Website Design team give an unforgettable impression on the customers and the clients. We can assure you that this is the best place for requirement of yours regarding website design solutions</p>
  <p>Brightlane Studio is a professional website design company dedicated to provide excellent services. We at Brightlane Studio think graphic design as a combination and collaboration of ideas and technology. Our Website Design team give an unforgettable impression on the customers and the clients. We can assure you that this is the best place for requirement of yours regarding website design solutions</p>
  <p>Brightlane Studio provides you the Search Engine Optimization making your website search engine friendly. So that the website can achieve top position and ranking in the Internet searches and thereby increasing the scope for the website to be found by customers. We here modify the site to improve the ranking by using the keywords and contents.</p>
  <div class="read-more">read more &rsaquo;</div>
</main>

<div class="sidebar-divider"></div>

<aside class="blog-feed">
  <h2 class="section-title">Recent Blog Feed <span class="feed-dot"></span></h2>
  <article class="post">
    <h3>Tittle Headline goes here</h3>
    <p>PixelMentors is elastic and extensible, providing our customers with all the necessary resources to complete their requirements on budget and on time.</p>
    <div class="post-meta">BY AUTHOR NAME<span>|</span>POSTED ON 20 MARCH 2012</div>
  </article>
  <article class="post">
    <h3>Tittle Headline goes here</h3>
    <p>PixelMentors is elastic and extensible, providing our customers with all the necessary resources to complete their requirements on budget and on time.</p>
    <div class="post-meta">BY AUTHOR NAME<span>|</span>POSTED ON 20 MARCH 2012</div>
  </article>
  <article class="post">
    <h3>Tittle Headline goes here</h3>
    <p>PixelMentors is elastic and extensible, providing our customers with all the necessary resources to complete their requirements on budget and on time.</p>
    <div class="post-meta">BY AUTHOR NAME<span>|</span>POSTED ON 20 MARCH 2012</div>
  </article>
</aside>

<footer class="site-footer">
  <div class="footer-links">Home<span>|</span>Web Development<span>|</span>Social Media<span>|</span>Server Management<span>|</span>Clouds Deployment<span>|</span>Code Review</div>
  <div class="copyright">Copyright © 2009-2012 PixelMentors Inc</div>
  <div class="social"><span></span><span></span><span></span></div>
</footer>

</body>
</html>
```